north lark upkeep services

Target Market(s)

General letter head for emails and letter quotes ect

Colors
0054AA
0677BA
7BADD7
CADEEF
E8F1F8
0094D4
00A9DD
6FCCEA
C7EBF8
E9F6FB

Requirements
Must have
• logo phone email website names
Nice to have
• what we do (from the website)

```html
<!DOCTYPE html>
<html lang="en">
<head>
<meta charset="utf-8">
<title>North Lark Upkeep Services – Letterhead</title>
<link rel="stylesheet" href="https://fonts.googleapis.com/css2?family=Open+Sans:wght@400;600;700&display=swap">
<style>
  :root {
    --bg: #ececec;
    --paper: #ffffff;
    --navy: #232a6e;
    --blue: #0677BA;
    --cyan: #00A9DD;
    --sky: #0094D4;
    --ink: #1c1c1c;
    --body: #9a9a9a;
    --rule: #a8a8a8;
    --sign-fill: #E8F1F8;
  }
  * { margin: 0; padding: 0; box-sizing: border-box; }
  html, body {
    width: 999px; height: 1200px; overflow: hidden;
    background: var(--bg);
    font-family: "Open Sans", Arial, sans-serif;
  }
  .letterhead {
    position: absolute; left: 71px; top: 0;
    width: 856px; height: 1200px;
    background: var(--paper);
  }
  .brand {
    position: absolute; left: 74px; top: 70px;
    display: flex; align-items: center; gap: 14px;
  }
  .brand-dot {
    width: 52px; height: 52px; border-radius: 50%;
    background: var(--blue); flex: none;
  }
  .brand-name {
    font-weight: 700; font-size: 21px; line-height: 1.2;
    color: var(--navy); width: 150px;
  }
  .header-rule { position: absolute; left: 60px; top: 244px; }
  .sender { position: absolute; left: 71px; top: 328px; color: var(--ink); }
  .sender-name { font-size: 22px; font-weight: 600; color: var(--navy); line-height: 1.2; }
  .sender-title { font-size: 12.5px; margin-bottom: 8px; }
  .sender-line { font-size: 15px; line-height: 24.5px; }
  .sender-line b { color: var(--cyan); font-weight: 700; margin-right: 6px; }
  .date {
    position: absolute; right: 66px; top: 421px;
    font-size: 15px; color: var(--ink);
  }
  .body-copy {
    position: absolute; left: 71px; top: 503px; width: 719px;
    font-size: 14.5px; line-height: 23.7px; color: var(--body);
  }
  .body-copy p { margin-bottom: 23.7px; }
  .body-copy span { display: block; white-space: nowrap; overflow: hidden; }
  .signature {
    position: absolute; left: 578px; top: 872px;
    width: 182px; height: 42px; border-radius: 4px;
    background: var(--sign-fill);
  }
  .signer {
    position: absolute; left: 570px; top: 924px; width: 200px;
    text-align: center; color: var(--ink);
  }
  .signer-name { font-size: 17px; font-weight: 700; line-height: 1.3; }
  .signer-role { font-size: 16px; line-height: 1.2; }
  .footer-line { position: absolute; top: 1091px; height: 3px; }
  .footer-line.left { left: 0; width: 96px; background: var(--sky); }
  .footer-line.right { left: 760px; width: 96px; background: var(--navy); }
  .contact-bar {
    position: absolute; left: 95px; top: 1073px;
    width: 665px; height: 39px; border-radius: 20px;
    background: linear-gradient(90deg, var(--navy) 0%, var(--blue) 55%, var(--cyan) 100%);
    display: flex; align-items: center; padding-left: 18px; gap: 20px;
    color: #fff; font-size: 15px;
  }
  .contact-item { display: flex; align-items: center; gap: 7px; white-space: nowrap; }
  .contact-icon {
    width: 20px; height: 20px; border-radius: 3px;
    background: var(--sky); display: flex; align-items: center; justify-content: center;
  }
</style>
</head>
<body>
<main class="letterhead">
  <header class="brand">
    <span class="brand-dot"></span>
    <span class="brand-name">North Lark Upkeep Services</span>
  </header>

  <svg class="header-rule" width="740" height="12" viewBox="0 0 740 12">
    <defs>
      <linearGradient id="ruleAccent" x1="0" x2="1">
        <stop offset="0" stop-color="#00A9DD"/>
        <stop offset="1" stop-color="#232a6e"/>
      </linearGradient>
    </defs>
    <polygon points="8,2 232,2 226,11 0,11" fill="url(#ruleAccent)"/>
    <line x1="228" y1="3" x2="738" y2="3" stroke="#a8a8a8" stroke-width="2"/>
  </svg>

  <section class="sender">
    <div class="sender-name">Clara Venn</div>
    <div class="sender-title">Chief Director</div>
    <div class="sender-line"><b>A :</b>12-3, Harbour Lane Singapore - 4410</div>
    <div class="sender-line"><b>W :</b>hello@northlark.com, www.northlark.com</div>
    <div class="sender-line"><b>P :</b>+65 - 61234 - 5501</div>
  </section>

  <div class="date">Date, 10 September, 2019</div>

  <article class="body-copy">
    <p>
      <span>This is a sample letter that has been placed to demonstrate typing remat (Your Company). letterhead</span>
      <span>design. When positioned properly, it will serve to work in harmony with all other elements letterhead.</span>
      <span>This letterhead design is meant to project an image</span>
    </p>
    <p>
      <span>This letterhead design is meant project an image of professionalism reliability. By using simple aligen</span>
      <span>we have created a very spacious feeling. The simplicity suggest  rengththe spaciousnes contributes h</span>
      <span>aesthetics the layout. These basic qualities along with the (Your Company)</span>
    </p>
    <p>
      <span>look and helps reinforce the (Your Company) brand. letterhead design is meant to project an image p</span>
      <span>design. When positioned properly, it will serve to work in harmony all the other elements letterhead.</span>
      <span>This letterhead design is meant project an image of professionalism reliability. By using simple aligen</span>
      <span>we have created a very spacious feeling. The simplicity suggest  rengththe spaciousnes contributes h</span>
      <span>aesthetics the layout. These basic qualities along with the (Your Company)</span>
    </p>
  </article>

  <div class="signature" role="img" aria-label="Handwritten signature of Owen Marsh"></div>
  <div class="signer">
    <div class="signer-name">Owen Marsh</div>
    <div class="signer-role">Manager</div>
  </div>

  <div class="footer-line left"></div>
  <div class="footer-line right"></div>
  <footer class="contact-bar">
    <span class="contact-item">
      <span class="contact-icon">
        <svg width="13" height="13" viewBox="0 0 24 24"><path fill="#fff" d="M6.6 10.8a15 15 0 0 0 6.6 6.6l2.2-2.2c.3-.3.7-.4 1-.2 1.1.4 2.3.6 3.6.6.6 0 1 .4 1 1V20c0 .6-.4 1-1 1A17 17 0 0 1 3 4c0-.6.4-1 1-1h3.5c.6 0 1 .4 1 1 0 1.3.2 2.5.6 3.6.1.3 0 .7-.2 1z"/></svg>
      </span>+65 6123 4550
    </span>
    <span class="contact-item">
      <span class="contact-icon">
        <svg width="13" height="13" viewBox="0 0 24 24"><rect x="2" y="5" width="20" height="14" rx="1.5" fill="#fff"/><path d="M2.5 6l9.5 7 9.5-7" fill="none" stroke="#0094D4" stroke-width="1.8"/></svg>
      </span>office@northlark.com
    </span>
    <span class="contact-item">
      <span class="contact-icon">
        <svg width="13" height="13" viewBox="0 0 24 24"><path fill="#fff" d="M5 2l14 11-6 1 3.5 7-2.5 1.2-3.5-7L6 19z"/></svg>
      </span>www.northlarkupkeep.com
    </span>
  </footer>
</main>
</body>
</html>
```